Membership Comparison Chart

I need the current membership chart recreated with additional perks listed at the bottom with our other companies, when you purchase a membership with us. Please remove the "curated cafe" at the bottom (has not opened yet). We are a shooting range and education center. This chart was originally created 2 years ago. I need in file form that is printable as well as a file that is able to be updated periodically. Please add the words "A Vantrop Group Company" below the logo attached.

```html
<!DOCTYPE html>
<html lang="en">
<head>
<meta charset="utf-8">
<title>Membership Comparison Chart</title>
<link href="https://fonts.googleapis.com/css2?family=Inter:wght@400;600;700;800&family=Oswald:wght@400;500;600;700&display=swap" rel="stylesheet">
<style>
:root{
  --red:#ed1c24;
  --red-elite:#d81e26;
  --red-plat:#b3161c;
  --panel:#4a4a4a;
  --row:#3e3e3e;
  --head-dark:#262626;
  --line:#5c5c5c;
  --white:#ffffff;
  --muted:#c9c9c9;
  --ink:#1a1a1a;
}
*{margin:0;padding:0;box-sizing:border-box}
html,body{width:927px;height:1200px;overflow:hidden;background:var(--white)}
body{position:relative;font-family:"Inter",Arial,sans-serif;color:var(--white)}

.hero{position:absolute;left:0;top:0;width:927px;height:171px;background:var(--red)}
.hero-band{position:absolute;right:0;top:171px;width:222px;height:55px;background:var(--red)}
.hero-mark{position:absolute;left:64px;top:40px;width:88px;height:88px;border-radius:50%;border:9px solid #2a2a2a}
.hero-text{position:absolute;left:165px;top:26px;font-family:"Oswald",sans-serif;white-space:nowrap}
.hero-kicker{font-size:14px;font-weight:600;letter-spacing:.3px;line-height:1.1}
.hero-title{font-size:30px;font-weight:700;line-height:1.05;letter-spacing:-.3px;margin-top:2px;padding-bottom:4px;border-bottom:2px solid var(--white);width:728px}
.hero-sub{font-size:22px;font-weight:600;margin-top:10px;line-height:1.1;letter-spacing:-.2px}
.hero-lede{font-size:20px;font-weight:400;margin-top:4px;line-height:1.1}

.panel{position:absolute;left:0;top:171px;width:705px;height:1029px;background:var(--panel);border-top-right-radius:16px}

.chart{position:absolute;left:36px;top:197px;width:635px;display:grid;grid-template-columns:230px 135px 135px 135px}
.chart > div{display:flex;flex-direction:column;justify-content:center;border-bottom:1px solid var(--line);background:var(--row)}
.cell{align-items:center;text-align:center;font-weight:700;font-size:16.5px;line-height:1.1}
.cell small{display:block;font-family:"Oswald",sans-serif;font-weight:400;font-size:11.5px;color:var(--muted);margin-top:3px;letter-spacing:.2px}
.cell.tight{font-size:14px}
.label{padding:0 8px;font-weight:700;font-size:14.6px;line-height:1.22}
.label span{font-weight:400;font-size:12.6px;display:block;line-height:1.25}
.label span.big{font-size:14.4px}

.chart > .brand{background:var(--head-dark);flex-direction:row;align-items:center;justify-content:flex-start;padding-left:12px;gap:8px;border-bottom:none}
.brand-dot{width:32px;height:32px;border-radius:50%;border:5px solid var(--white);flex:none}
.brand-name{font-size:14px;font-weight:600;line-height:1.1;text-transform:uppercase;letter-spacing:.2px}
.brand-parent{display:block;font-size:9px;font-weight:400;letter-spacing:.3px;color:var(--red);margin-top:3px}
.chart > .tier{align-items:center;text-align:center;border-bottom:none;font-weight:800;font-size:21px;line-height:1}
.tier span{display:block;font-weight:400;font-size:12.5px;margin-top:3px}
.chart > .basic{background:var(--red)}
.chart > .elite{background:var(--red-elite)}
.chart > .plat{background:var(--red-plat)}
.tick{width:14px;height:14px;opacity:.25}

.perks{position:absolute;left:705px;top:226px;width:222px;height:974px;color:var(--ink);font-family:"Oswald",sans-serif}
.perks-head{position:absolute;top:38px;left:0;width:222px;text-align:center;font-weight:700;font-size:20px;line-height:1.28}
.perks-arrow{position:absolute;left:75px;top:160px}
.perk{position:absolute;left:16px;width:194px;display:flex;align-items:center;gap:8px}
.perk p{font-size:11.5px;line-height:1.1;text-align:center;font-weight:500;flex:1}
.perk p em{font-style:normal;font-weight:400;display:block}
.badge{flex:none;background:#2b2b2b}
.perk-green{flex-direction:column;gap:5px}
.perk-green .row{display:flex;align-items:center;gap:8px}
.perk-green .name{font-weight:700;font-size:17px;line-height:1;color:#3d3d3d}
.perk-nb .name{color:#c8102e;font-weight:700;font-size:14px;line-height:1;text-align:center}
.promise{position:absolute;left:10px;top:800px;width:202px;text-align:center}
.promise-brand{display:flex;align-items:center;justify-content:center;gap:5px;font-size:10px;font-weight:600;line-height:1.05;text-transform:uppercase;text-align:left}
.promise-dot{width:18px;height:18px;border-radius:50%;border:3px solid var(--ink);flex:none}
.promise-parent{font-size:9px;font-weight:400;color:#c8102e;margin-top:3px;letter-spacing:.3px}
.promise h3{font-size:18px;font-weight:700;margin-top:4px}
.promise p{font-family:"Inter",sans-serif;font-size:10px;line-height:1.22;margin-top:3px}
</style>
</head>
<body>

<header class="hero">
  <div class="hero-mark"></div>
  <div class="hero-text">
    <div class="hero-kicker">FEATURING</div>
    <div class="hero-title">THE WORLD'S LARGEST INDOOR DOUBLE-DECK GUN RANGE</div>
    <div class="hero-sub">Digital Assault Survival Theater, and 20+ Safety-Focused Classes,</div>
    <div class="hero-lede">our membership gives you unbeatable value...</div>
  </div>
</header>
<div class="hero-band"></div>

<section class="panel"></section>

<section class="chart">
  <div class="brand" style="height:72px"><div class="brand-dot"></div><div class="brand-name">Ridgeline Armory<br>Shooting Center<span class="brand-parent">A Vantrop Group Company</span></div></div>
  <div class="tier basic">BASIC<span>MEMBERSHIP</span></div>
  <div class="tier elite">ELITE<span>MEMBERSHIP</span></div>
  <div class="tier plat">PLATINUM<span>MEMBERSHIP</span></div>

  <div class="label" style="height:81px">Family Gun &amp; Archery Range Use<span>You, your spouse and all children under 18. 21 Gun Salute Range</span></div>
  <div class="cell">FREE<small>UNLIMITED USE</small></div>
  <div class="cell">FREE<small>UNLIMITED USE</small></div>
  <div class="cell">FREE<small>UNLIMITED USE</small></div>

  <div class="label" style="height:49px">FREE Firearm Lesson Level<span>tailored to your experience</span></div>
  <div class="cell">-</div>
  <div class="cell">FREE LESSON</div>
  <div class="cell">FREE LESSON</div>

  <div class="label" style="height:48px">FREE Archery Lesson Level<span>tailored to your experience</span></div>
  <div class="cell">-</div>
  <div class="cell">FREE LESSON</div>
  <div class="cell">FREE LESSON</div>

  <div class="label" style="height:49px">5% OFF All Firearms</div>
  <div class="cell">-</div>
  <div class="cell tight">STOCK AND<br>SPECIAL ORDER</div>
  <div class="cell tight">STOCK AND<br>SPECIAL ORDER</div>

  <div class="label" style="height:51px">Digital Assault Survival and Fun Target Theaters</div>
  <div class="cell">25% OFF</div>
  <div class="cell">50% OFF</div>
  <div class="cell">FREE 12<br>HOURS</div>

  <div class="label" style="height:64px">10% OFF Everything Else<span>(Ammo, Holsters, Targets, Gun Bags, etc.)</span></div>
  <div class="cell">10% OFF</div>
  <div class="cell">10% OFF</div>
  <div class="cell">10% OFF</div>

  <div class="label" style="height:52px">Required Master Carrier Target</div>
  <div class="cell">10% OFF</div>
  <div class="cell">10% OFF</div>
  <div class="cell">1 FREE<small>EVERY VISIT</small></div>

  <div class="label" style="height:69px">Discounts on RASC Training*<span class="big">Dozens of Basic and Advanced Classes</span></div>
  <div class="cell">25% OFF</div>
  <div class="cell">50% OFF<small>PLUS 2 FREE REPEATS</small></div>
  <div class="cell">1 FREE/VISIT<small>PLUS 10 FREE REPEATS</small></div>

  <div class="label" style="height:67px">Free Guest Passes Per Year Sharing Lane With member</div>
  <div class="cell">5 FREE<small>YEARLY</small></div>
  <div class="cell">10 FREE<small>YEARLY</small></div>
  <div class="cell" style="font-size:15px">1 FREE / VISIT<small>PLUS 10 FREE FOR<br>GIFTING*</small></div>

  <div class="label" style="height:51px">Gun Rentals</div>
  <div class="cell">50% OFF</div>
  <div class="cell">FREE</div>
  <div class="cell">FREE<small>FOR MEMBER &amp; GUEST</small></div>

  <div class="label" style="height:52px">Discount on FFL Transfer</div>
  <div class="cell">$10 OFF</div>
  <div class="cell">$15 OFF</div>
  <div class="cell">FREE<small>UNLIMITED</small></div>

  <div class="label" style="height:70px">NO Credit Card Hold for Lanes Firearm Deposit Required</div>
  <div class="cell"><svg class="tick" viewBox="0 0 14 14"><path d="M2 7.5l3 3 7-8" fill="none" stroke="#fff" stroke-width="2"/></svg></div>
  <div class="cell"><svg class="tick" viewBox="0 0 14 14"><path d="M2 7.5l3 3 7-8" fill="none" stroke="#fff" stroke-width="2"/></svg></div>
  <div class="cell"><svg class="tick" viewBox="0 0 14 14"><path d="M2 7.5l3 3 7-8" fill="none" stroke="#fff" stroke-width="2"/></svg></div>

  <div class="label" style="height:34px">Free Meeting/Party Room</div>
  <div class="cell">1 Hr</div>
  <div class="cell">5 Hrs</div>
  <div class="cell">10 Hrs</div>

  <div class="label" style="height:52px">Refer New Member Reward</div>
  <div class="cell">$10<small>GIFT CARD</small></div>
  <div class="cell">$20<small>GIFT CARD</small></div>
  <div class="cell">$25<small>GIFT CARD</small></div>

  <div class="label" style="height:107px">COST Plus 1-time $100 Initiation Fee<span>(No Fee if Paid in Full with Cash)</span></div>
  <div class="cell">$35/MONTH<small>$520 TOTAL</small><span style="margin-top:3px">SINGLE<br>PAYMENT</span><small>$420 TOTAL</small></div>
  <div class="cell">$55/MONTH<small>$760 TOTAL</small><span style="margin-top:3px">SINGLE<br>PAYMENT</span><small>$660 TOTAL</small></div>
  <div class="cell">$79 /MONTH<small>$1048 TOTAL</small><span style="margin-top:3px">SINGLE<br>PAYMENT</span><small>$948 TOTAL</small></div>
</section>

<aside class="perks">
  <div class="perks-head">PLUS THESE<br>EXTRA BENEFITS<br>YOU NEVER<br>EXPECTED.</div>
  <svg class="perks-arrow" width="72" height="23" viewBox="0 0 72 23"><path d="M0 0h72L36 23z" fill="#ed1c24"/></svg>

  <div class="perk" style="top:205px"><div class="badge" style="width:44px;height:44px;border-radius:50%"></div><p>5 FREE OUTDOOR INDOOR COURT PASSES<em>(PUNCH CARD)</em><em>Lakeshore Pickleball Center</em></p></div>

  <div class="perk" style="top:320px"><div class="badge" style="width:48px;height:48px;border-radius:50%;background:#e6e6e6"></div><p>5% OFF SOCIAL EVENTS AND WEDDING PACKAGES<em>(VENUE RENTAL)</em><em>Hillcrest Venue</em></p></div>

  <div class="perk perk-green" style="top:420px">
    <div class="row"><div class="badge" style="width:44px;height:44px;background:#6cc04a"></div><div class="name">VERDANT<br>YARD CO</div></div>
    <p>50% OFF DELIVERY FEE FOR MULCH, STONE, TOPSOIL.<br>5% OFF CONCRETE, BASEMENT WATERPROOFING, SNOW MITIGATION, OR LAWN CARE</p>
  </div>

  <div class="perk perk-nb" style="top:600px;flex-direction:column;gap:4px"><div class="name">NORTHGATE INDUSTRIAL<br>TECH CENTER</div><p>10% OFF FIRST MONTH PAYMENT WITH A 1-YEAR LEASE</p></div>

  <div class="promise">
    <div class="promise-brand"><div class="promise-dot"></div><div>Ridgeline Armory<br>Shooting Center<div class="promise-parent">A Vantrop Group Company</div></div></div>
    <h3>OUR PROMISE</h3>
    <p>We will do everything in our power to support our members' wellness health, and safety with education and training in a state-of-the-art facility.</p>
  </div>
</aside>

</body>
</html>
```